Consulting Website

We are looking at renewing out company's website. we are an organizational development consulting firm that works within the Middle East and Africa. Our focus on on organizations within the Gulf area.

We are looking to having a simple, clean and attractive website. pictures should be relevant to our location.

We are also looking for a creative design, something that isn't just "another consulting website"
Updates

Thank you all for submitting your designs, following are some general comments;

- Having a veiled women on the intro is NOT a must
- have a picture with people is NOT a must too, we can use nature, symbols, places..anything really!
- Here are some sites i like;
mivanorth.example
http://www.brellokhomes.example/
http://www.quistavarn.example/
http://www.zorebin.example/

I hope these could give you some idea :)

thanks again.

Industry/Entity Type

It Company

Requirements
Must have
• Tabs for press, testimonials, products, resources and services.
pictures also should be relevant to the geographical location. i.e. veiled women, men in traditional costumes and so on.

It's very important that we MAINTAIN the corporate colors of the logo.
Should not have
• Clean and neat design!
i REALLY dont like crowded designs.

```html
<!DOCTYPE html>
<html lang="en">
<head>
<meta charset="utf-8">
<title>Veralta Consulting</title>
<link href="https://fonts.googleapis.com/css2?family=Source+Sans+3:ital,wght@0,400;0,600;1,400&display=swap" rel="stylesheet">
<style>
:root{
  --slate:#5b6d7e;
  --slate-dark:#4a5b6b;
  --slate-mid:#7f93a5;
  --slate-light:#a7b6c3;
  --accent:#c2664a;
  --text:#5a5a5a;
  --link:#4d6275;
  --page:#f1f1f1;
  --white:#ffffff;
  --rule:#c9c9c9;
  --arrow:#4a9fd8;
}
*{box-sizing:border-box;margin:0;padding:0}
html,body{width:1061px;height:1200px;overflow:hidden}
body{font-family:"Source Sans 3",sans-serif;color:var(--text);background:var(--white);position:relative}
ul{list-style:none}

/* top navigation */
.topnav{position:absolute;left:0;top:0;width:1061px;height:61px;background:linear-gradient(#65778a,var(--slate) 70%,#52626f)}
.topnav a{position:absolute;top:0;height:61px;line-height:61px;color:var(--white);font-size:14px;text-decoration:none}
.topnav .current{left:44px;width:82px;text-align:center;background:var(--slate-dark)}
.topnav .current::after{content:"";position:absolute;left:35px;bottom:-8px;border:6px solid transparent;border-top-color:var(--slate-dark);border-bottom:0}
.search{position:absolute;left:789px;top:13px;width:199px;height:30px;background:var(--white);border:1px solid #c9d0d6;border-radius:3px;padding:0 12px;font-size:12px;font-style:italic;line-height:28px;color:#888}
.search svg{position:absolute;right:9px;top:9px}

/* header */
.masthead{position:absolute;left:0;top:61px;width:1061px;height:374px;background:repeating-linear-gradient(45deg,#f3f3f3 0 2px,#eeeeee 2px 4px);border-bottom:1px solid #dedede}
.brand{position:absolute;left:44px;top:34px;display:flex;align-items:center;gap:12px}
.brand-mark{width:62px;height:62px;background:var(--slate-mid)}
.brand-name{font-size:40px;font-weight:400;color:var(--slate);letter-spacing:1px;line-height:1}
.phone{position:absolute;right:66px;top:54px;font-size:21px;color:var(--slate)}
.hero{position:absolute;left:48px;top:122px;width:952px;height:227px;border:2px solid var(--slate-mid);border-radius:6px;overflow:hidden;background:linear-gradient(100deg,#a08466,#c8a57f 45%,#b8956e 70%,#d0b089)}
.hero svg{position:absolute;left:0;bottom:0}
.login{position:absolute;left:14px;bottom:14px;display:flex;align-items:center;gap:8px;color:var(--white);font-size:14px}
.login i{width:24px;height:28px;border-radius:12px 12px 4px 4px;background:#e6d6c3;display:block}

/* sidebar */
.sidebar{position:absolute;left:44px;top:453px;width:224px}
.side-title{font-size:18px;color:var(--link);font-weight:400}
.products{margin:14px 0 0 10px}
.products li{font-size:12px;color:var(--link);line-height:24px;padding-left:16px;position:relative}
.products li::before{content:"";position:absolute;left:0;top:10px;width:4px;height:4px;border-radius:50%;background:var(--link)}
.side-rule{border:0;border-top:1px solid var(--rule);margin:14px 0 12px -2px}
.testimonials-head{display:flex;justify-content:space-between;align-items:center}
.quote{margin:22px 0 0 12px;font-size:12px;font-style:italic;line-height:17px;position:relative;padding-left:12px}
.quote::before{content:"";position:absolute;left:0;top:7px;width:4px;height:4px;border-radius:50%;background:var(--text)}
.quote-author{text-align:right;font-size:12px;font-weight:600;color:#333;margin-top:6px}
.press{margin-top:22px;width:222px;height:212px;border-radius:4px;background:linear-gradient(#a1b2c1,var(--slate-mid) 45%,#5f7386);color:var(--white);padding:0 14px;position:relative}
.press-head{height:34px;line-height:32px;text-align:center;font-size:17px;color:#3f4f5e;background:#c2ced8;margin:0 -10px;border-radius:0 0 50% 50%/0 0 80% 80%}
.press-head svg{position:absolute;right:22px;top:5px}
.release{margin-top:16px;font-size:11.5px;line-height:14px}
.release b{display:block;font-weight:600;font-size:12px;margin-bottom:6px}
.view-all{position:absolute;right:12px;bottom:10px;font-size:12px;color:var(--white);text-decoration:underline}
.col-rule{position:absolute;left:289px;top:453px;width:1px;height:600px;background:var(--rule)}

/* main */
.main{position:absolute;left:309px;top:448px;width:697px}
.heading{font-size:21px;font-weight:400;color:var(--accent)}
.main p{font-size:11.3px;line-height:18px}
.intro{margin-top:13px}
.lead{color:var(--accent);font-size:11.5px;margin-top:6px}
.benefits{display:grid;grid-template-columns:312px 1fr;margin:4px 0 0 12px}
.benefits li{font-size:11.5px;line-height:24px;padding-left:26px;position:relative}
.benefits li svg{position:absolute;left:0;top:7px}
.dashed{border:0;border-top:1px dashed #8a8a8a;margin:22px 0 18px}
.resources{display:flex;gap:26px;margin-top:10px}
.resources-text{width:436px;position:relative}
.service-lists{display:flex;gap:0;margin:14px 0 0 16px}
.service-lists ul{width:171px}
.service-lists li{font-size:11.5px;line-height:24px;color:#333;padding-left:14px;position:relative}
.service-lists li::before{content:"";position:absolute;left:0;top:10px;width:4px;height:4px;border-radius:50%;background:#333}
.view-more{position:absolute;right:2px;bottom:4px;height:20px;line-height:20px;padding:0 8px;border-radius:3px;background:linear-gradient(#8596a6,#5e7183);color:var(--white);font-size:11px}
.resources-photo{width:232px;height:155px;border:3px solid #d8d8d8;background:linear-gradient(#8d9677,#6f7564 40%,#3b3b3f)}

/* footer */
.footer{position:absolute;left:0;top:1094px;width:1061px;height:106px;background:var(--slate);color:var(--white)}
.footer-links{position:absolute;top:22px;width:100%;text-align:center;font-size:11.5px}
.footer-links span{margin:0 6px;color:#c6d0d9}
.copyright{position:absolute;left:45px;top:64px;font-size:11.5px}
.social{position:absolute;right:57px;top:59px;display:flex;gap:7px}
.social i{width:24px;height:24px;border-radius:50%;background:var(--white);display:block}
</style>
</head>
<body>

<nav class="topnav">
  <a class="current">Home</a>
  <a style="left:147px">About VERALTA »</a>
  <a style="left:287px">Offerings »</a>
  <a style="left:392px">Knowledge Base »</a>
  <a style="left:540px">Contact us</a>
  <div class="search">Search
    <svg width="10" height="10" viewBox="0 0 10 10"><circle cx="4" cy="4" r="3" fill="none" stroke="#aaa" stroke-width="1.3"/><line x1="6.2" y1="6.2" x2="9" y2="9" stroke="#aaa" stroke-width="1.5"/></svg>
  </div>
</nav>

<header class="masthead">
  <div class="brand"><span class="brand-mark"></span><span class="brand-name">VERALTA</span></div>
  <div class="phone">Call Us : +971 4000 2750</div>
  <div class="hero" role="img" aria-label="Photo of three women in headscarves in front of a sandstone wall">
    <svg width="420" height="110" viewBox="0 0 420 110"><path d="M0 0 C20 60 150 95 420 110 L0 110 Z" fill="#6b8197" opacity=".85"/></svg>
    <div class="login"><i></i>Log in</div>
  </div>
</header>

<aside class="sidebar">
  <h2 class="side-title">Products</h2>
  <ul class="products">
    <li>Consectetur adipiscing elit</li>
    <li>Phasellus pretium dolor aclibero</li>
    <li>Vivamus et nunc id</li>
    <li>Maecenas aliquet nisi malesuada</li>
    <li>Consectetur adipiscing elit</li>
    <li>Phasellus pretium dolor aclibero</li>
    <li>Vivamus et nunc id</li>
    <li>Maecenas aliquet nisi malesuada</li>
  </ul>
  <hr class="side-rule">
  <div class="testimonials-head">
    <h2 class="side-title">Testimonials</h2>
    <svg width="22" height="12" viewBox="0 0 22 12"><path d="M6 1 1 6l5 5M16 1l5 5-5 5" fill="none" stroke="#555" stroke-width="1.5"/></svg>
  </div>
  <p class="quote">Neque porro quisquam est, qui dolorem ipsum quia dolor sit amet, consectetur, adipisci velit...</p>
  <p class="quote-author">Facilisis venenatis</p>
  <section class="press">
    <h2 class="press-head">Press Releases
      <svg width="14" height="22" viewBox="0 0 14 22"><path d="M2 8 7 3l5 5M2 14l5 5 5-5" fill="none" stroke="#4a5b6b" stroke-width="1.5"/></svg>
    </h2>
    <div class="release"><b>February 15th, 2012</b>Aui dolorem ipsum quia dolor sit amet, consectetur, adipisci velit.</div>
    <div class="release"><b>February 15th, 2012</b>Aui dolorem ipsum quia dolor sit amet, consectetur, adipisci velit.</div>
    <a class="view-all">View all</a>
  </section>
</aside>
<div class="col-rule"></div>

<main class="main">
  <h1 class="heading">Welcome to our site</h1>
  <p class="intro">Veralta Consulting is a firm specialized in providing customized Organization Development solutions to companies in the Middle East and Africa. Recognizing the inability of imported models and solutions to solve problems that face companies in our region, Veralta Consulting builds on international best practices and customizes them to create best-fit solutions that are capable of addressing challenges effectively. Veralta Consulting provides Organization Development solutions addressing the "HOW – Soft Side" that is needed to achieve the "WHAT – Business Strategy" in a holistic manner. Veralta Consulting work centers around building an organizational culture that is aligned with and supports the business strategy.</p>
  <p class="lead">Veralta Consulting helps organization develop an aligned humanistic organization design that:</p>
  <ul class="benefits">
    <li><svg width="14" height="10" viewBox="0 0 14 10"><path d="M0 3h8V0l6 5-6 5V7H0z" fill="var(--arrow)"/></svg>Creates a culture of high performance</li>
    <li><svg width="14" height="10" viewBox="0 0 14 10"><path d="M0 3h8V0l6 5-6 5V7H0z" fill="var(--arrow)"/></svg>Increases internal organization efficiencies</li>
    <li><svg width="14" height="10" viewBox="0 0 14 10"><path d="M0 3h8V0l6 5-6 5V7H0z" fill="var(--arrow)"/></svg>Nurtures leaders &amp; builds human potential</li>
    <li><svg width="14" height="10" viewBox="0 0 14 10"><path d="M0 3h8V0l6 5-6 5V7H0z" fill="var(--arrow)"/></svg>Enhances organization agility</li>
    <li><svg width="14" height="10" viewBox="0 0 14 10"><path d="M0 3h8V0l6 5-6 5V7H0z" fill="var(--arrow)"/></svg>Induces innovation across all corporate practices</li>
  </ul>
  <p style="margin-top:4px">Veralta Consulting utilizes a collaborative consulting model in which consultants work hand in hand with our clients to help them build organizations that support achieving the business strategy. They support clients with the implementation of change initiatives and, most importantly, transfer knowledge and build internal client capability to lead future change programs.</p>
  <p>At Veralta Consulting, we believe that change can only happen when leadership, people and culture within the organization are open and willing to make this change; therefore in our efforts to implement major changes within the organization, Veralta Consulting uses a culture lens as a major mean to see through the organization and makes its organizational change decisions accordingly.</p>
  <hr class="dashed">
  <h2 class="heading">Resources and Services</h2>
  <div class="resources">
    <div class="resources-text">
      <p>Neque porro quisquam est, qui dolorem ipsum quia dolor sit amet, consectetur, adipisci velit, sed quia non numquam eius modi tempora incidunt ut labore et dolore magnam aliquam quaerat voluptatem.</p>
      <div class="service-lists">
        <ul><li>consectetur adipiscing</li><li>Phasellus pretium</li><li>Vivamus et nunc</li><li>Maecenas aliquet</li></ul>
        <ul><li>consectetur adipiscing</li><li>Phasellus pretium</li><li>Vivamus et nunc</li><li>Maecenas aliquet</li></ul>
      </div>
      <span class="view-more">View more</span>
    </div>
    <div class="resources-photo" role="img" aria-label="Photo of a group of women in abayas walking down an outdoor path"></div>
  </div>
</main>

<footer class="footer">
  <div class="footer-links">Home<span>|</span>About VERALTA<span>|</span>Offerings<span>|</span>Knowledge Base<span>|</span>Contact us<span>|</span>Sitemap</div>
  <div class="copyright">Copyright © 2012 www.veralta.example &nbsp; All rights reserved</div>
  <div class="social" aria-label="Social links"><i></i><i></i><i></i><i></i><i></i></div>
</footer>

</body>
</html>
```